stationary deign for trucking company

im a trucking company looking for a professional set of stationary designs i deliver goods from point a to b
Updates

When submitting stationary designs I need envelope design, letterhead, cards, I’d badge etc

Industry/Entity Type

Trucking Company

Requirements
Must have
• must have letter head, business card, envelope, fax sheet, id badge, folder, thank you card, notebook, invoice sheet.
Nice to have
• nice to have them all custom made (letterhead,envelope, business card, I’d badge etc
Should not have
• must not have prepaid sign want i unique design for items

```html
<!DOCTYPE html>
<html lang="en">
<head>
<meta charset="utf-8">
<title>Harlow Transportation + Logistics – Business Card</title>
<link href="https://fonts.googleapis.com/css2?family=Poppins:wght@400;500;600&display=swap" rel="stylesheet">
<style>
  :root {
    --bg: #ecebe8;
    --card-dark: #242526;
    --card-light: #ffffff;
    --brand-blue: #1b5cc4;
    --ink: #1d1d1f;
    --ink-soft: #3c3c40;
    --rule: #4a5a7a;
  }
  html, body {
    margin: 0;
    padding: 0;
    width: 1200px;
    height: 920px;
    overflow: hidden;
    background: var(--bg);
    font-family: "Poppins", sans-serif;
  }
  .canvas {
    position: relative;
    width: 1200px;
    height: 920px;
  }
  .card {
    position: absolute;
    top: 315px;
    width: 540px;
    height: 300px;
    box-shadow: 0 6px 14px rgba(0,0,0,0.25);
    overflow: hidden;
  }
  .card-back {
    left: 40px;
    background: var(--card-dark);
    display: flex;
    align-items: center;
    justify-content: center;
  }
  .back-wordmark {
    display: flex;
    align-items: center;
    gap: 18px;
    color: var(--brand-blue);
    font-weight: 600;
    font-size: 52px;
    letter-spacing: 4px;
  }
  .back-wordmark .mark-square {
    width: 34px;
    height: 34px;
    background: var(--brand-blue);
  }
  .card-front {
    left: 624px;
    background: var(--card-light);
  }
  .front-wordmark {
    position: absolute;
    top: 58px;
    right: 36px;
    display: flex;
    align-items: center;
    gap: 12px;
    color: var(--ink);
    font-weight: 600;
    font-size: 28px;
    letter-spacing: 3px;
  }
  .front-wordmark .mark-square {
    width: 22px;
    height: 22px;
    background: var(--ink);
  }
  .name-accent {
    position: absolute;
    left: 0;
    top: 166px;
    width: 6px;
    height: 30px;
    background: var(--brand-blue);
  }
  .person-name {
    position: absolute;
    left: 30px;
    top: 163px;
    margin: 0;
    color: var(--brand-blue);
    font-weight: 600;
    font-size: 19px;
    letter-spacing: 0.3px;
  }
  .person-title {
    position: absolute;
    left: 30px;
    top: 190px;
    margin: 0;
    color: var(--ink-soft);
    font-size: 12px;
  }
  .divider {
    position: absolute;
    left: 30px;
    top: 216px;
    width: 470px;
    height: 1px;
    background: var(--rule);
  }
  .divider::before {
    content: "";
    position: absolute;
    left: 0;
    top: -1px;
    width: 140px;
    height: 2px;
    background: var(--brand-blue);
  }
  .contact-list {
    position: absolute;
    left: 30px;
    top: 228px;
    margin: 0;
    padding: 0;
    list-style: none;
    font-size: 12.5px;
    color: var(--ink);
  }
  .contact-list li {
    display: flex;
    align-items: center;
    gap: 12px;
    height: 19.5px;
  }
  .contact-list svg {
    width: 11px;
    height: 11px;
    fill: none;
    stroke: var(--brand-blue);
    stroke-width: 1.6;
  }
  .office-address {
    position: absolute;
    right: 40px;
    top: 228px;
    margin: 0;
    text-align: right;
    font-style: normal;
    font-size: 12.5px;
    line-height: 19.5px;
    color: var(--ink);
  }
  .office-address .office-name {
    color: var(--brand-blue);
    font-weight: 600;
  }
  .bottom-band {
    position: absolute;
    left: 0;
    bottom: 0;
    width: 250px;
    height: 5px;
    background: var(--brand-blue);
  }
</style>
</head>
<body>
<div class="canvas">

  <section class="card card-back" aria-label="Business card back">
    <div class="back-wordmark">
      <span class="mark-square"></span>
      <span>HARLOW</span>
    </div>
  </section>

  <section class="card card-front" aria-label="Business card front">
    <div class="front-wordmark">
      <span class="mark-square"></span>
      <span>HARLOW</span>
    </div>

    <span class="name-accent"></span>
    <h1 class="person-name">DALE CORWIN</h1>
    <p class="person-title">Senior Consultant</p>
    <span class="divider"></span>

    <ul class="contact-list">
      <li>
        <svg viewBox="0 0 12 12"><path d="M2 1.5 L4.2 1.5 L5 4 L3.8 5 Q5 7.5 7 8.2 L8 7 L10.5 7.8 L10.5 10 Q5 10.5 2 4.5 Z" fill="#1b5cc4" stroke="none"/></svg>
        <span>(402) 555-0148</span>
      </li>
      <li>
        <svg viewBox="0 0 12 12"><rect x="1" y="2.5" width="10" height="7"/><path d="M1 2.5 L6 6.5 L11 2.5"/></svg>
        <span>info@harlowfreight.com</span>
      </li>
      <li>
        <svg viewBox="0 0 12 12"><circle cx="6" cy="6" r="4.8"/><path d="M1.2 6 H10.8 M6 1.2 Q3.5 6 6 10.8 M6 1.2 Q8.5 6 6 10.8"/></svg>
        <span>www.harlowfreight.com</span>
      </li>
    </ul>

    <address class="office-address">
      <span class="office-name">HARLOW</span><br>
      418 W Elm St. Ste 210<br>
      Dayton, OH 45402
    </address>

    <span class="bottom-band"></span>
  </section>

</div>
</body>
</html>
```